Real Estate Investor needs awesome business card design

I invest in real estate, focused on multi-family properties, and I need a business card to hand out to potential partners. I prefer simple, clean designs, but it needs to stand out, so I'd like there to be a bit of red in the design as well.

It should include this information:

Front
Dallin Pecksworth
Real Estate Investor
Direct phone: 502-867-3394
Email: dallinhpecksworth@quillmail.example
Headshot (Picture), I've uploaded a few, just pick the one you think looks best with your design. You can remove the background from the headshot image if it looks better.

Back
The back of the card's design should flow and be congruent with the front. On the back I want to put an inspirational quote or question. There will be different ones depending on the card, so I'll need the original file so I can edit it in the end.

For now, use “The Pessimist Sees Difficulty In Every Opportunity. The Optimist Sees The Opportunity In Every Difficulty.” -Barnaby Ellsworth

Target Market(s)

Investors

Industry/Entity Type

Real Estate

Contact Information for Business Card

Front
Dallin Pecksworth
Real Estate Investor

Back
The back of the card's design should flow and be congruent with the front. On the back I want to put an inspirational quote or question. There will be different ones depending on the card, so I'll need the original file so I can edit it in the end. I've uploaded some EXAMPLES of business cards with quotes on them. Don't copy but feel free to use them as inspiration.

The design will be printed on "ZIB sized" business cards
1039 x 697 pixels
with rounded corners

Font styles to use
Serif
Decorative
Script

Colors
ec1f27

Requirements
Must have
• Headshot, name, and other information in it.
• 1039 x 697 pixels
• Rounded corners
• Clean design that pops. I'm open to see any color background, including black.
• Headshots can be located here: https://www.filecrate.example/sh/8kd2wq7mzt31hvx/BBQTXP4ruf9LmQ0KhcvWx7b?dl=0
Nice to have
• It would be awesome if the design included a personal signature or monogram, but if not I'll get a personal logo developed later and the card redesigned if I think it needs it.
Should not have
• Cluttered design

```html
<!DOCTYPE html>
<html lang="en">
<head>
<meta charset="utf-8">
<title>Dallin Pecksworth — Business Card</title>
<link rel="stylesheet" href="https://fonts.googleapis.com/css2?family=Josefin+Sans:wght@300;400&family=Open+Sans:ital,wght@0,400;1,400&display=swap">
<style>
  :root {
    --page-bg: #e9e6e1;
    --card-white: #ffffff;
    --card-black: #050505;
    --ink: #151515;
    --ink-light: #f2f2f2;
    --accent-red: #ec1f27;
    --photo-dark: #1a1a1a;
    --photo-mid: #5a5a5a;
  }
  * { box-sizing: border-box; margin: 0; padding: 0; }
  html, body {
    width: 1200px;
    height: 1200px;
    overflow: hidden;
    background: var(--page-bg);
  }
  .sheet {
    width: 1200px;
    height: 1200px;
    display: flex;
    flex-direction: column;
    align-items: center;
    justify-content: center;
    gap: 40px;
  }
  .card {
    position: relative;
    width: 820px;
    height: 550px;
    border-radius: 28px;
    overflow: hidden;
    box-shadow: 0 6px 18px rgba(0,0,0,0.12);
  }

  /* Front */
  .card--front {
    background: var(--card-white);
    color: var(--ink);
    display: flex;
    align-items: center;
    justify-content: center;
  }
  .front-block {
    display: flex;
    flex-direction: column;
    align-items: flex-start;
  }
  .headshot {
    width: 240px;
    height: 150px;
    border-radius: 10px;
    background: radial-gradient(ellipse at 35% 45%, var(--photo-mid) 0%, #333 40%, var(--photo-dark) 100%);
    margin-bottom: 26px;
  }
  .name-group {
    display: flex;
    flex-direction: column;
    align-items: flex-end;
    margin-bottom: 26px;
  }
  .front-name {
    font-family: "Josefin Sans", sans-serif;
    font-weight: 400;
    font-size: 34px;
    letter-spacing: 1.5px;
    text-transform: uppercase;
    line-height: 1;
    white-space: nowrap;
  }
  .front-title {
    margin-top: 6px;
    font-family: "Open Sans", sans-serif;
    font-size: 15px;
    color: var(--accent-red);
  }
  .front-phone {
    font-family: "Josefin Sans", sans-serif;
    font-weight: 300;
    font-size: 32px;
    letter-spacing: 2px;
    line-height: 1;
    margin-bottom: 24px;
  }
  .front-email {
    font-family: "Open Sans", sans-serif;
    font-size: 20px;
    letter-spacing: 0.3px;
    white-space: nowrap;
  }

  /* Back */
  .card--back {
    background: linear-gradient(135deg, #151515 0%, var(--card-black) 45%, #0d0d0d 100%);
    color: var(--ink-light);
    padding: 90px 70px 0;
  }
  .back-heading {
    display: inline-flex;
    flex-direction: column;
    align-items: flex-end;
  }
  .back-name {
    font-family: "Josefin Sans", sans-serif;
    font-weight: 300;
    font-size: 56px;
    letter-spacing: 3px;
    text-transform: uppercase;
    line-height: 1;
    white-space: nowrap;
  }
  .back-title {
    margin-top: 10px;
    font-family: "Open Sans", sans-serif;
    font-size: 28px;
    letter-spacing: 1px;
    color: var(--accent-red);
    line-height: 1.2;
  }
  .back-quote {
    margin-top: 70px;
    width: 560px;
    font-family: "Open Sans", sans-serif;
    font-style: italic;
    font-size: 17px;
    line-height: 1.55;
    letter-spacing: 0.4px;
  }
  .back-quote cite { display: block; font-style: italic; }
</style>
</head>
<body>
  <main class="sheet">
    <section class="card card--front" aria-label="Card front">
      <div class="front-block">
        <div class="headshot" role="img" aria-label="Black and white headshot of Dallin Pecksworth"></div>
        <div class="name-group">
          <h1 class="front-name">Dallin Pecksworth</h1>
          <p class="front-title">Real Estate Investor</p>
        </div>
        <p class="front-phone">502-867-3394</p>
        <p class="front-email">dallinhpecksworth@quillmail.example</p>
      </div>
    </section>

    <section class="card card--back" aria-label="Card back">
      <div class="back-heading">
        <h2 class="back-name">Dallin Pecksworth</h2>
        <p class="back-title">Real Estate Investor</p>
      </div>
      <blockquote class="back-quote">
        The Pessimist Sees Difficulty In Every Opportunity. The Optimist Sees The Opportunity In Every Difficulty.
        <cite>-Barnaby Ellsworth-</cite>
      </blockquote>
    </section>
  </main>
</body>
</html>
```